Harbourlight Geriatric care need Business card design

Simple and elegance looking business card (colour choice will be very important)
Harbourlight geriatric care is medical consultation service for elderly population.

1st side---business logo and the doctor name/tile
eg: dr. XXX
MBBS,FRACP etc
Main room:
suite xxx AAA medical centre 18 XXX road Vic 3000
Phone:
Fax:

2nd side --different clinic address (up to 3 addresses) and need to have appointment time/ date

Suite xxx AAA medical centre , 18 XXX road VIC 3000

Please see attachment for business logo

Important: need to be compatible with Quillo Press for printing purpose.

Thank you.

hi, please look at the sample business card and create something similar. Company name: Harbourlight Geriatric Care PTY LTD ABN 47580916 ( all small font and no need to be obvious) company logo need to be obvious Apart from steadfast in support, also add Geriatrician for Community and Residential Care. Main room Pondaro Medical Centre suite 2.07 204-206 Larkspur street Box Hill Vic All appointment and enquiries: tel: 908716252 Fasmile: www.qwvplmzk.com.au Tindlewood Medical Centre 42 gorrington road mooroolbark VIC Bayview Crest Private Frankston 87 Pellworth road , franskton VIC 3199 Oakrun Private Hospital specialist room 259 Dunmore Road, Mt. Waverley VIC 3333 Dr. TM 81920kp DR. RH w7169208nd DR. PJ 670918vt Thank you

```html
<!DOCTYPE html>
<html lang="en">
<head>
<meta charset="utf-8">
<title>Harbourlight Geriatric Care – Business Card</title>
<link href="https://fonts.googleapis.com/css2?family=Arimo:ital,wght@0,400;0,700;1,400;1,700&display=swap" rel="stylesheet">
<style>
  :root{
    --navy:#1f2b66;
    --navy-deep:#18234f;
    --white:#ffffff;
    --paper:#f4f4f6;
    --ink:#1c1c24;
    --muted:#6b6f7a;
    --soft:#c9cde0;
    --backdrop-a:#4a5661;
    --backdrop-b:#2a333b;
    --red:#c8202c;
  }
  *{box-sizing:border-box;margin:0;padding:0}
  html,body{width:1200px;height:1000px;overflow:hidden}
  body{
    font-family:"Arimo",Arial,sans-serif;
    background:radial-gradient(ellipse at 50% 40%,var(--backdrop-a),var(--backdrop-b));
    position:relative;
  }
  .card{
    position:absolute;left:240px;width:720px;height:440px;
    overflow:hidden;box-shadow:0 14px 30px rgba(0,0,0,.45);
  }
  /* ---------- back side ---------- */
  .card--back{top:40px;background:var(--white)}
  .doctor-picks{
    height:62px;display:flex;align-items:center;justify-content:space-between;
    padding:0 40px;color:var(--navy);font-weight:700;font-size:17px;
  }
  .pick{display:flex;align-items:center;gap:12px}
  .box{
    display:inline-block;width:18px;height:18px;border:2px solid var(--ink);
    box-shadow:2px 2px 0 var(--ink);background:var(--white);flex:none;
  }
  .clinics{
    height:180px;background:var(--navy);color:var(--white);
    display:grid;grid-template-columns:1fr 1fr;padding:16px 36px 0 40px;gap:0 20px;
  }
  .clinic{margin-bottom:14px;font-size:15px;line-height:1.25}
  .clinic__name{font-weight:700;font-style:italic;font-size:15px}
  .brand--back{display:flex;align-items:center;gap:12px;margin-top:18px}
  .brand__dot{width:34px;height:34px;border-radius:50%;background:var(--white);flex:none}
  .brand__name{font-size:22px;font-weight:400;color:var(--white)}
  .brand__tag{font-size:9px;letter-spacing:3px;color:var(--white);margin-left:46px;margin-top:2px}
  .appointment{display:grid;grid-template-columns:1fr 1fr;padding:22px 40px 0;color:var(--ink)}
  .appointment__lead{font-size:18px;margin-bottom:14px}
  .venues{display:grid;grid-template-columns:1fr 1fr;gap:16px 10px;font-weight:700;font-size:18px}
  .venue{display:flex;align-items:center;gap:14px}
  .slots{display:flex;flex-direction:column;gap:16px;padding-left:20px}
  .slot{display:flex;align-items:center;gap:12px;font-size:18px}
  .slot svg{width:20px;height:20px;flex:none}
  .slot__label{width:58px}
  .slot__line{flex:1;border-bottom:1.5px solid var(--ink);height:16px}
  /* ---------- front side ---------- */
  .card--front{top:520px;background:var(--navy)}
  .front-top{display:flex;height:300px}
  .front-brand{
    width:46%;background:linear-gradient(160deg,var(--white),var(--paper));
    padding:18px 24px 0;position:relative;text-align:center;
  }
  .abn{font-size:13px;color:var(--muted);text-align:left}
  .brand--front{margin-top:38px;display:flex;flex-direction:column;align-items:center}
  .brand--front .brand__dot{width:78px;height:78px;background:var(--navy);margin-bottom:20px}
  .brand--front .brand__name{color:var(--navy);font-size:25px;font-weight:700}
  .brand--front .brand__tag{color:var(--muted);margin:4px 0 0;letter-spacing:4px;font-size:10px}
  .front-brand__service{color:var(--navy);font-size:17px;line-height:1.35;margin-top:12px}
  .front-doctor{flex:1;color:var(--white);padding:36px 26px 0}
  .doctor__name{font-size:24px;font-weight:700}
  .doctor__quals{font-size:15px;color:var(--soft);margin-top:4px}
  .doctor__role{font-size:18px;line-height:1.4;margin-top:4px}
  .main-room{margin-top:40px}
  .main-room__title{font-size:19px;font-weight:700;font-style:italic;color:var(--soft)}
  .main-room__addr{font-size:16px;line-height:1.5;color:var(--soft);margin-top:4px}
  .front-footer{
    height:140px;border-top:4px solid var(--white);background:var(--navy-deep);
    color:var(--white);text-align:center;padding-top:16px;
  }
  .company{font-size:15px;letter-spacing:3px}
  .contact{font-size:20px;margin-top:10px}
  .contact em{font-style:italic}
  .web{font-size:19px;margin-top:10px}
  .web b{font-weight:700}
</style>
</head>
<body>

<section class="card card--back" aria-label="Card back: clinics and appointment">
  <div class="doctor-picks">
    <span class="pick"><span class="box"></span>Dr. Tomas Merrin</span>
    <span class="pick"><span class="box"></span>Dr. Name Here</span>
    <span class="pick"><span class="box"></span>Dr. Name Here</span>
  </div>
  <div class="clinics">
    <div>
      <div class="clinic">
        <div class="clinic__name">Tindlewood Medical Centre</div>
        42, Gorrington Road<br>Mooroolbark, VIC 0000
      </div>
      <div class="clinic">
        <div class="clinic__name">Oakrun Private Hospital</div>
        Specialist Room, 259 Dunmore Road<br>Mt. Waverley, VIC 3333
      </div>
    </div>
    <div>
      <div class="clinic">
        <div class="clinic__name">Bayview Crest Private Frankston</div>
        87, Pellworth Road,<br>Franskton, VIC 3199
      </div>
      <div class="brand brand--back">
        <span class="brand__dot"></span>
        <span class="brand__name">Harbourlight Geriatric Care</span>
      </div>
      <div class="brand__tag">STEADFAST IN SUPPORT</div>
    </div>
  </div>
  <div class="appointment">
    <div>
      <p class="appointment__lead">Your next appointment has been made at:</p>
      <div class="venues">
        <span class="venue"><span class="box"></span>Pondaro</span>
        <span class="venue"><span class="box"></span>Tindlewood</span>
        <span class="venue"><span class="box"></span>Bayview</span>
        <span class="venue"><span class="box"></span>Oakrun</span>
      </div>
    </div>
    <div class="slots">
      <div class="slot">
        <svg viewBox="0 0 20 20" aria-hidden="true"><rect x="2" y="3" width="16" height="15" rx="2" fill="none" stroke="#7f86a8" stroke-width="1.6"/><rect x="2" y="3" width="16" height="4" fill="#7f86a8"/></svg>
        <span class="slot__label">Day:</span><span class="slot__line"></span>
      </div>
      <div class="slot">
        <svg viewBox="0 0 20 20" aria-hidden="true"><rect x="2" y="3" width="16" height="15" rx="2" fill="none" stroke="#7f86a8" stroke-width="1.6"/><rect x="2" y="3" width="16" height="4" fill="#7f86a8"/><g fill="#7f86a8"><rect x="5" y="9" width="2" height="2"/><rect x="9" y="9" width="2" height="2"/><rect x="13" y="9" width="2" height="2"/><rect x="5" y="13" width="2" height="2"/><rect x="9" y="13" width="2" height="2"/><rect x="13" y="13" width="2" height="2"/></g></svg>
        <span class="slot__label">Date:</span><span class="slot__line"></span>
      </div>
      <div class="slot">
        <svg viewBox="0 0 20 20" aria-hidden="true"><circle cx="10" cy="10" r="8" fill="none" stroke="#7f86a8" stroke-width="1.6"/><path d="M10 5v5l3 2" fill="none" stroke="#7f86a8" stroke-width="1.6"/></svg>
        <span class="slot__label">Time:</span><span class="slot__line"></span>
      </div>
    </div>
  </div>
</section>

<section class="card card--front" aria-label="Card front: logo and doctor details">
  <div class="front-top">
    <div class="front-brand">
      <p class="abn">ABN 47580916</p>
      <div class="brand brand--front">
        <span class="brand__dot"></span>
        <span class="brand__name">Harbourlight Geriatric Care</span>
        <span class="brand__tag">STEADFAST IN SUPPORT</span>
      </div>
      <p class="front-brand__service">Geriatrician for Community<br>and Residential Care</p>
    </div>
    <div class="front-doctor">
      <h1 class="doctor__name">Dr. Tomas Merrin</h1>
      <p class="doctor__quals">MBBS, FRACP, Clin Dip Pall Care</p>
      <p class="doctor__role">Consultant physician<br>and Geriatrician</p>
      <div class="main-room">
        <p class="main-room__title">Main Room - Pondaro Medical Centre</p>
        <p class="main-room__addr">Suite 2.07 204-206, Level 3<br>Larkspur Street Box Hill, VIC 3128</p>
      </div>
    </div>
  </div>
  <div class="front-footer">
    <p class="company">HARBOURLIGHT GERIATRIC CARE PTY LTD</p>
    <p class="contact"><em>All Appointments &amp; Enquiries:</em> Tel (03) 9087 1625 Fax (03) 8419 2703</p>
    <p class="web">www.<b>qwvplmzk</b>.com.au</p>
  </div>
</section>

</body>
</html>
```